Kitchen Tools Infographic - Helpful Items for Healthy Home Meals

We are a weight loss company that provides holistic, natural nutrition programs to consumers -- you can see our web site at www.FernQuill.com. We need a simple infographic to be shared on social media and via email. The topic for the infographic is "Equip Your Kitchen for Healthy Home Meals". We've outlined 5 groups of kitchen tools that are helpful for consumers to have for preparing home meals, and included some framing statistics emphasizing the weight management benefits of preparing meals versus eating out.

Target Market(s)

Women age 35-55

Industry/Entity Type

Health And Wellness

Font styles to use
Sans Serif

Colors
0292cd
9bcb3b

Requirements
Must have
• - FernQuill Logo
• - Graphics summarizing statistic (weight gain)
• - Graphics showing groupings of kitchen tools
Should not have
• body scale graphics
• before/after graphics

```html
<!DOCTYPE html>
<html lang="en">
<head>
<meta charset="utf-8">
<title>Equip Your Kitchen for Healthy Home Meals — FernQuill</title>
<link href="https://fonts.googleapis.com/css2?family=Oswald:wght@400;500&family=Roboto:wght@300;400;500&family=Kaushan+Script&display=swap" rel="stylesheet">
<style>
:root{
  --teal:#0bb3c9;
  --teal-dark:#07899b;
  --green:#8cc63f;
  --green-dark:#6fa22b;
  --ink:#555a5e;
  --ink-soft:#7a7f83;
  --panel:#f6f6f6;
  --header-grey:#efefef;
  --number-grey:#c9c9c9;
  --line:#e1e1e1;
  --footer:#e6e5e0;
  --white:#ffffff;
}
*{box-sizing:border-box;margin:0;padding:0}
html,body{width:1200px;height:2985px;overflow:hidden}
body{position:relative;background:var(--white);font-family:'Roboto',Arial,sans-serif;color:var(--ink)}
.abs{position:absolute}

/* hero */
.hero{left:0;top:0;width:1200px;height:300px}
.hero-photo{position:absolute;inset:0;background:linear-gradient(100deg,#8a8f86 0%,#b8b5ab 30%,#a89f92 55%,#7d6a58 80%,#a0522d 100%)}
.hero-shade{position:absolute;inset:0;background:rgba(40,40,40,.18)}
.title-ribbon{position:absolute;left:300px;top:36px;width:600px;height:110px}
.title-main{position:absolute;left:0;top:48px;width:1200px;text-align:center;font-family:'Oswald',sans-serif;font-weight:500;font-size:44px;letter-spacing:2px;color:var(--white)}
.title-for{position:absolute;left:0;top:150px;width:1200px;text-align:center;font-family:'Kaushan Script',cursive;font-size:38px;color:var(--white)}
.title-sub{position:absolute;left:0;top:212px;width:1200px;text-align:center;font-family:'Oswald',sans-serif;font-size:42px;letter-spacing:3px;color:var(--white)}

/* why cook */
.why{left:0;top:300px;width:1200px;height:760px;background:var(--panel)}
.why-title{position:absolute;top:52px;width:100%;text-align:center;font-size:26px;color:var(--green);font-weight:400}
.why-text{position:absolute;top:130px;left:180px;width:840px;text-align:center;font-size:16px;line-height:30px;font-weight:300;color:#444}
.chart-ribbon{position:absolute;top:262px;height:50px}
.chart-ribbon span{position:absolute;inset:0;display:flex;align-items:center;justify-content:center;font-family:'Oswald',sans-serif;font-size:21px;color:var(--white);letter-spacing:.5px}
.chart{position:absolute;top:340px}
.chart text{font-family:'Roboto',sans-serif;font-size:13px;fill:#666}

/* tools */
.tools-title{left:0;top:1100px;width:1200px;text-align:center;font-size:33px;font-weight:300;color:#444}
.tool-card{position:absolute;top:1204px;width:190px;height:1180px;border:1px solid var(--line);background:var(--white)}
.card-number{position:absolute;left:0;top:0;width:100%;height:140px;background:var(--header-grey);clip-path:polygon(0 0,100% 0,100% 100px,50% 136px,0 100px);
  text-align:center;font-family:'Oswald',sans-serif;font-size:52px;color:var(--number-grey);padding-top:20px}
.card-band{position:absolute;left:0;top:126px;width:100%;height:200px;clip-path:polygon(0 0,50% 36px,100% 0,100% 100%,0 100%);
  display:flex;align-items:center;justify-content:center;padding-top:30px;font-family:'Oswald',sans-serif;font-size:50px;color:var(--white)}
.band-teal{background:var(--teal)}
.band-green{background:var(--green)}
.card-items{position:absolute;left:0;top:356px;width:100%}
.tool{height:262px;text-align:center;padding:0 10px}
.tool-icon{display:block;margin:0 auto 14px;width:90px;height:90px;border-radius:10px}
.icon-teal{background:linear-gradient(160deg,#bfe9f0,#6fcfdc)}
.icon-green{background:linear-gradient(160deg,#d6ecb4,#a8d46a)}
.tool-name{font-family:'Oswald',sans-serif;font-size:16px;color:var(--teal);text-transform:uppercase;margin-bottom:8px}
.tool-desc{font-size:15px;line-height:21px;color:#555;font-weight:300}

/* footer */
.cta-ribbon{left:140px;top:2452px;width:920px;height:70px}
.cta-ribbon span{position:absolute;inset:0;display:flex;align-items:center;justify-content:center;font-size:26px;color:var(--white);font-weight:400}
.cta-ribbon b{font-weight:500;margin-right:8px}
.invite{left:0;top:2556px;width:1200px;text-align:center;font-family:'Kaushan Script',cursive;font-size:32px;color:#6a6a6a}
.contact{left:516px;top:2640px;width:168px;height:70px;background:var(--teal);color:var(--white);font-family:'Roboto',sans-serif;font-weight:500;font-size:20px;display:flex;align-items:center;justify-content:center}
.brand{left:0;top:2780px;width:1200px;display:flex;align-items:center;justify-content:center;gap:12px}
.brand-dot{width:26px;height:26px;border-radius:50%;background:var(--green)}
.brand-name{font-family:'Roboto',sans-serif;font-weight:500;font-size:34px;color:var(--teal);letter-spacing:1px}
.site{left:0;top:2852px;width:1200px;text-align:center;font-size:22px;color:var(--teal)}
.sources{left:0;top:2910px;width:1200px;height:75px;background:var(--footer);padding:10px 0 0 62px;font-size:12px;line-height:26px;color:#777}
.sources .indent{padding-left:58px}
</style>
</head>
<body>

<header class="abs hero">
  <div class="hero-photo" role="img" aria-label="Kitchen counter photo with fresh basil, tomatoes and vegetables"></div>
  <div class="hero-shade"></div>
  <svg class="title-ribbon" viewBox="0 0 600 110" aria-hidden="true">
    <polygon points="0,20 70,20 70,100 0,100 24,60" fill="var(--teal-dark)"/>
    <polygon points="600,20 530,20 530,100 600,100 576,60" fill="var(--teal-dark)"/>
    <rect x="40" y="0" width="520" height="90" fill="var(--teal)"/>
  </svg>
  <h1 class="title-main">EQUIP YOUR KITCHEN</h1>
  <div class="title-for">for</div>
  <div class="title-sub">HEALTHY HOME MEALS</div>
</header>

<section class="abs why">
  <h2 class="why-title">Why Cook at Home?</h2>
  <p class="why-text">Those who eat out consume an average of 134 calories more per meal. &nbsp;Americans eat out an average of 4.5 times per week, so those extra calories can add up to substantial weight gain -- and give you a reason to prepare your own meals.</p>

  <svg class="chart-ribbon" style="left:72px;width:480px" viewBox="0 0 480 50" aria-hidden="true">
    <polygon points="0,0 480,0 462,25 480,50 0,50 18,25" fill="var(--teal)"/>
  </svg>
  <div class="chart-ribbon" style="left:72px;width:480px"><span>EXCESS CALORIES FROM RESTAURANT MEALS</span></div>

  <svg class="chart-ribbon" style="left:650px;width:480px" viewBox="0 0 480 50" aria-hidden="true">
    <polygon points="0,0 480,0 462,25 480,50 0,50 18,25" fill="var(--teal)"/>
  </svg>
  <div class="chart-ribbon" style="left:650px;width:480px"><span>POUNDS GAINED FROM RESTAURANT MEALS</span></div>

  <svg class="chart" style="left:160px" width="340" height="380" viewBox="0 0 340 380" role="img" aria-label="Bar chart: 134 extra calories per meal, 603 per week">
    <g stroke="#e4e4e4" stroke-width="1">
      <line x1="66" y1="310" x2="320" y2="310"/><line x1="66" y1="258" x2="320" y2="258"/>
      <line x1="66" y1="206" x2="320" y2="206"/><line x1="66" y1="154" x2="320" y2="154"/>
      <line x1="66" y1="102" x2="320" y2="102"/><line x1="66" y1="50" x2="320" y2="50"/>
    </g>
    <line x1="66" y1="40" x2="66" y2="362" stroke="#ccc"/>
    <line x1="66" y1="362" x2="320" y2="362" stroke="#ccc"/>
    <g text-anchor="end">
      <text x="56" y="314">100</text><text x="56" y="262">200</text><text x="56" y="210">300</text>
      <text x="56" y="158">400</text><text x="56" y="106">500</text><text x="56" y="54">600</text>
    </g>
    <rect x="118" y="292" width="28" height="70" fill="var(--green)"/>
    <rect x="244" y="49" width="28" height="313" fill="var(--green)"/>
    <g text-anchor="middle">
      <text x="132" y="380">Calories per</text>
      <text x="258" y="380">Calories per</text>
    </g>
  </svg>
  <div class="abs" style="left:270px;top:722px;width:120px;text-align:center;font-size:13px;color:#666">Meal</div>
  <div class="abs" style="left:388px;top:722px;width:120px;text-align:center;font-size:13px;color:#666">Week</div>

  <svg class="chart" style="left:690px" width="360" height="380" viewBox="0 0 360 380" role="img" aria-label="Bar chart: about 3 pounds gained in 2 months, 4.6 in 6 months, 9 in 1 year">
    <g stroke="#e4e4e4" stroke-width="1">
      <line x1="50" y1="310" x2="340" y2="310"/><line x1="50" y1="258" x2="340" y2="258"/>
      <line x1="50" y1="206" x2="340" y2="206"/><line x1="50" y1="154" x2="340" y2="154"/>
      <line x1="50" y1="102" x2="340" y2="102"/><line x1="50" y1="50" x2="340" y2="50"/>
    </g>
    <line x1="50" y1="40" x2="50" y2="362" stroke="#ccc"/>
    <line x1="50" y1="362" x2="340" y2="362" stroke="#ccc"/>
    <g text-anchor="end">
      <text x="40" y="314">2</text><text x="40" y="262">4</text><text x="40" y="210">6</text>
      <text x="40" y="158">8</text><text x="40" y="106">10</text><text x="40" y="54">12</text>
    </g>
    <rect x="94" y="284" width="28" height="78" fill="var(--green)"/>
    <rect x="182" y="242" width="28" height="120" fill="var(--green)"/>
    <rect x="270" y="128" width="28" height="234" fill="var(--green)"/>
    <g text-anchor="middle">
      <text x="108" y="380">2 months</text><text x="196" y="380">6 months</text><text x="284" y="380">1 year</text>
    </g>
  </svg>
</section>

<h2 class="abs tools-title">Make Healthy Eating Easier With These Kitchen Tools</h2>

<article class="tool-card" style="left:72px">
  <div class="card-number">01</div>
  <div class="card-band band-teal">PREP</div>
  <div class="card-items">
    <div class="tool"><span class="tool-icon icon-teal" role="img" aria-label="Cutting board icon"></span><div class="tool-name">Cutting Board</div><p class="tool-desc">essential for prepping meat and vegetables</p></div>
    <div class="tool"><span class="tool-icon icon-teal" role="img" aria-label="Chef's knife icon"></span><div class="tool-name">Chef's Knife</div><p class="tool-desc">go for quality to make chopping, dicing and slicing faster and easier</p></div>
    <div class="tool"><span class="tool-icon icon-teal" role="img" aria-label="Digital food scale icon"></span><div class="tool-name">Digital Food Scale</div><p class="tool-desc">get the precision you need for perfect recipes and portion control</p></div>
  </div>
</article>

<article class="tool-card" style="left:290px">
  <div class="card-number">02</div>
  <div class="card-band band-green">TECH</div>
  <div class="card-items">
    <div class="tool"><span class="tool-icon icon-green" role="img" aria-label="Blender icon"></span><div class="tool-name">High-Powered Blender</div><p class="tool-desc">make highly nutritious, healthy drinks from fruits and veggies</p></div>
    <div class="tool"><span class="tool-icon icon-green" role="img" aria-label="Slow cooker icon"></span><div class="tool-name">Slow Cooker</div><p class="tool-desc">cook delicious meals while you are at work</p></div>
    <div class="tool"><span class="tool-icon icon-green" role="img" aria-label="Pressure cooker icon"></span><div class="tool-name">Pressure Cooker</div><p class="tool-desc">create single pot meals in 20 minutes or less</p></div>
  </div>
</article>

<article class="tool-card" style="left:508px">
  <div class="card-number">03</div>
  <div class="card-band band-teal">COOK</div>
  <div class="card-items">
    <div class="tool"><span class="tool-icon icon-teal" role="img" aria-label="Ceramic pan icon"></span><div class="tool-name">Ceramic Pan</div><p class="tool-desc">nonstick cooking surface allows you to cook without oil</p></div>
    <div class="tool"><span class="tool-icon icon-teal" role="img" aria-label="Vegetable steamer icon"></span><div class="tool-name">Vegetable Steamer</div><p class="tool-desc">preserve nutrients and natural, fresh taste</p></div>
    <div class="tool"><span class="tool-icon icon-teal" role="img" aria-label="Baking sheet icon"></span><div class="tool-name">Baking Sheet</div><p class="tool-desc">ideal for roasting vegetables in the oven or baking chicken and fish dishes</p></div>
  </div>
</article>

<article class="tool-card" style="left:726px">
  <div class="card-number">04</div>
  <div class="card-band band-green">SERVE</div>
  <div class="card-items">
    <div class="tool"><span class="tool-icon icon-green" role="img" aria-label="Cloth napkins icon"></span><div class="tool-name">Cloth Napkins</div><p class="tool-desc">to reduce waste and dress up your table</p></div>
    <div class="tool"><span class="tool-icon icon-green" role="img" aria-label="Dinnerware icon"></span><div class="tool-name">Dinnerware</div><p class="tool-desc">pre-plate meals rather than serving family style to control portions</p></div>
    <div class="tool"><span class="tool-icon icon-green" role="img" aria-label="Small plates icon"></span><div class="tool-name">Small Plates</div><p class="tool-desc">use salad plates and smaller dishware to manage perception of food volume</p></div>
  </div>
</article>

<article class="tool-card" style="left:944px">
  <div class="card-number">05</div>
  <div class="card-band band-teal">STORE</div>
  <div class="card-items">
    <div class="tool"><span class="tool-icon icon-teal" role="img" aria-label="Glass storage containers icon"></span><div class="tool-name">Glass Storage Containers</div><p class="tool-desc">keep your healthy left-overs so nothing goes to waste</p></div>
    <div class="tool"><span class="tool-icon icon-teal" role="img" aria-label="Mason jar icon"></span><div class="tool-name">Mason Jars</div><p class="tool-desc">perfect for premade salads that you can bring to work</p></div>
    <div class="tool"><span class="tool-icon icon-teal" role="img" aria-label="Freezer bag icon"></span><div class="tool-name">Freezer Safe Re-Sealable Bags</div><p class="tool-desc">prepare double batches to make the most of your time</p></div>
  </div>
</article>

<svg class="abs cta-ribbon" viewBox="0 0 920 70" aria-hidden="true">
  <polygon points="0,0 920,0 896,35 920,70 0,70 24,35" fill="var(--teal)"/>
</svg>
<div class="abs cta-ribbon"><span><b>FernQuill</b> can help you develop healthier eating habits</span></div>

<p class="abs invite">We invite you to learn more.</p>
<div class="abs contact">CONTACT US</div>

<div class="abs brand"><span class="brand-dot"></span><span class="brand-name">FERNQUILL</span></div>
<div class="abs site">www.FernQuill.com</div>

<footer class="abs sources">
  <div>Sources: &nbsp;https://www.harvestdata-review.org/2010/june/eating-out-increases-daily-calorie-intake/</div>
  <div class="indent">https://www.tablesurvey.net/b/the-state-of-home-dining-in-2016</div>
</footer>

</body>
</html>
```